Keys to a Successful Retirement

We have an audience of 175 who will be viewing these slides. They are designed to be "visual aids" to the presentation -- not a hand out. I am uploading the power point that I did --- we want a professional look but want to keep the words on the slides as they are. We want to keep the social security logo we pasted and the Dorrance logo, (our firm). Other than that, feel free to swap out pictures if you have better ones. We want to remain in Power Point so that we can edit it as necessary and display using our existing computers.

```html
<!DOCTYPE html>
<html lang="en">
<head>
<meta charset="utf-8">
<title>Dorrance Financial Group – Presentation Slides</title>
<link rel="stylesheet" href="https://fonts.googleapis.com/css2?family=Figtree:wght@300;400;600;700;800&display=swap">
<style>
  :root {
    --navy: #1b3c6e;
    --navy-deep: #123064;
    --band-light: #2a5db0;
    --ink: #3a3a3a;
    --grey-text: #4a4a4a;
    --rule: #b9b9b9;
    --slide-top: #ffffff;
    --slide-bottom: #e6e6e6;
    --canvas: #000000;
    --row-light: #ffffff;
    --row-alt: #f0f0f0;
    --cat-row: #cfcfcf;
    --head-grey: #a9a9a9;
    --opt1: #1b3c6e;
    --opt1-alt: #3d5f92;
    --opt2: #4a4a4a;
    --opt2-alt: #6a6a6a;
  }
  * { box-sizing: border-box; margin: 0; padding: 0; }
  html, body { width: 1061px; height: 1200px; overflow: hidden; background: var(--canvas); }
  body { font-family: "Figtree", Arial, sans-serif; color: var(--grey-text); }

  .deck {
    display: grid;
    grid-template-columns: 517px 517px;
    grid-template-rows: 388px 388px 388px;
    gap: 9px;
    padding: 9px;
    width: 1061px; height: 1200px;
  }
  .slide {
    position: relative;
    overflow: hidden;
    background: linear-gradient(180deg, var(--slide-top) 0%, var(--slide-bottom) 100%);
  }
  .slide::before {
    content: ""; position: absolute; left: 0; top: 0; right: 0; height: 8px; background: var(--navy);
  }
  .rule { position: absolute; height: 1px; background: var(--rule); }

  .slide-heading {
    position: absolute; left: 22px; top: 20px;
    font-size: 29px; font-weight: 700; color: var(--ink); letter-spacing: -0.2px;
  }
  .slide-heading .accent { color: var(--navy); }
  .slide-heading::before {
    content: ""; position: absolute; left: -22px; top: 9px; width: 13px; height: 20px; background: var(--navy);
  }

  .brand {
    font-family: "Figtree", Arial, sans-serif;
    font-weight: 700; color: var(--navy); letter-spacing: 1.5px; text-transform: uppercase;
  }

  .slide-footer { position: absolute; left: 0; right: 0; bottom: 0; height: 38px; }
  .slide-footer .rule { left: 14px; right: 14px; top: 0; }
  .slide-footer .brand { position: absolute; left: 22px; top: 11px; font-size: 13px; }
  .pager { position: absolute; right: 14px; top: 8px; display: flex; align-items: center; gap: 4px; }
  .pager svg { width: 22px; height: 20px; display: block; }
  .pager .sep { width: 1px; height: 20px; background: var(--rule); margin: 0 10px 0 8px; }
  .pager .num { font-size: 13px; color: var(--grey-text); }

  /* Title slide */
  .cover-title { position: absolute; left: 0; right: 0; top: 80px; text-align: center; }
  .cover-title .main { font-size: 50px; font-weight: 800; color: var(--ink); line-height: 1; letter-spacing: 0.5px; }
  .cover-title .main .accent { color: var(--navy); }
  .cover-title .sub { font-size: 39px; font-weight: 300; color: var(--ink); margin-top: 6px; }
  .cover-title .sub .accent { color: var(--navy); }
  .cover-brand { position: absolute; left: 42px; top: 252px; font-size: 20px; }
  .presenter { position: absolute; right: 42px; top: 247px; text-align: right; font-size: 13px; color: var(--grey-text); line-height: 1.3; }
  .presenter strong { display: block; font-size: 15px; color: var(--navy); font-weight: 700; }
  .blue-band {
    position: absolute; left: 0; right: 0; bottom: 0; height: 90px;
    background: linear-gradient(90deg, var(--navy-deep) 0%, var(--band-light) 50%, var(--navy-deep) 100%);
  }
  .blue-band svg { position: absolute; left: 242px; top: 15px; }

  /* About */
  .about-body { position: absolute; left: 22px; right: 22px; top: 72px; font-size: 14.2px; line-height: 19px; text-align: justify; }
  .about-body p { margin-bottom: 12px; }
  .about-body b { color: var(--navy); font-weight: 600; }

  /* Services */
  .service-list { position: absolute; left: 42px; top: 64px; list-style: none; }
  .service-list li { font-size: 18px; line-height: 25px; color: var(--ink); padding-left: 20px; position: relative; }
  .service-list li::before {
    content: ""; position: absolute; left: 2px; top: 9px; width: 7px; height: 7px; background: var(--navy); transform: rotate(45deg);
  }
  .team-photo {
    position: absolute; left: 238px; top: 86px; width: 260px; height: 216px;
    background: radial-gradient(ellipse at 50% 45%, #3b3b40 0%, #2a2a2e 40%, rgba(230,230,230,0) 72%);
  }

  /* Table */
  .option-table { position: absolute; left: 23px; top: 72px; width: 471px; border-collapse: collapse; font-size: 10px; }
  .option-table th { height: 25px; font-size: 14px; font-weight: 700; text-align: center; }
  .option-table th.cat { background: var(--head-grey); color: var(--ink); width: 235px; }
  .option-table th.o1 { background: var(--opt1); color: #fff; width: 118px; }
  .option-table th.o2 { background: var(--opt2); color: #fff; width: 118px; }
  .option-table td { height: 18px; }
  .option-table .category td { background: var(--cat-row); font-weight: 700; font-size: 10.5px; padding-left: 12px; color: var(--ink); }
  .option-table .item td:first-child { padding-left: 28px; background: var(--row-light); }
  .option-table .item:nth-child(odd) td:first-child { background: var(--row-alt); }
  .option-table td.o1 { background: var(--opt1); color: #fff; text-align: center; font-size: 11px; }
  .option-table td.o2 { background: var(--opt2); color: #fff; text-align: center; }
  .option-table .item.alt td.o1 { background: var(--opt1-alt); }
  .option-table .item.alt td.o2 { background: var(--opt2-alt); }

  /* Contact */
  .map-frame {
    position: absolute; left: 32px; top: 74px; width: 221px; height: 218px;
    background: #fff; border: 1px solid #cfcfcf; padding: 5px;
  }
  .map-frame div { width: 100%; height: 100%; background: linear-gradient(160deg, #dfe6cf 0%, #cfd9b6 45%, #a8c7df 60%, #d8dcc4 100%); }
  .contact-info { position: absolute; left: 267px; top: 73px; right: 20px; font-size: 9.4px; line-height: 11.5px; }
  .contact-info .intro { text-align: justify; margin-bottom: 8px; }
  .contact-info .intro b { color: var(--navy); }
  .contact-info h3 { font-size: 12px; color: var(--navy); font-weight: 600; margin-top: 6px; line-height: 14px; }
  .social { position: absolute; left: 42px; top: 313px; display: flex; align-items: center; gap: 9px; }
  .social span.box { width: 18px; height: 18px; background: var(--navy); border-radius: 2px; }
  .social .handle { font-size: 12px; font-weight: 600; color: var(--navy); margin-left: 2px; }

  /* Thank you */
  .thanks { position: absolute; left: 0; right: 0; top: 84px; text-align: center; font-size: 76px; font-weight: 800; color: var(--ink); letter-spacing: -2px; }
  .thanks .accent { color: var(--navy); }
  .thanks-brand { position: absolute; left: 0; right: 0; top: 236px; text-align: center; font-size: 22px; }
</style>
</head>
<body>
<main class="deck">

  <section class="slide slide-cover">
    <div class="rule" style="left:42px; right:42px; top:52px;"></div>
    <div class="cover-title">
      <div class="main"><span class="accent">TITLE</span> PROJECT</div>
      <div class="sub">subtext <span class="accent">presentation</span></div>
    </div>
    <div class="rule" style="left:42px; right:42px; top:220px;"></div>
    <div class="brand cover-brand">Dorrance</div>
    <div class="presenter">Presentation by<strong>Alan Reyes</strong></div>
    <div class="blue-band">
      <svg width="34" height="60" viewBox="0 0 34 60" aria-hidden="true"><path d="M0 0 L14 0 L34 30 L14 60 L0 60 L20 30 Z" fill="#fff"/></svg>
    </div>
  </section>

  <section class="slide slide-about">
    <h2 class="slide-heading"><span class="accent">About</span> Company</h2>
    <div class="about-body">
      <p><b>Lorem ipsum</b> dolor sit amet, consectetuer adipiscing elit. Maecenas porttitor congue massa. Fusce posuere, magna sed pulvinar ultricies, purus lectus malesuada libero, sit amet commodo magna eros quis urna.</p>
      <p><b>Nunc viverra imperdiet enim</b>. Fusce est. Vivamus a tellus. Pellentesque habitant morbi tristique senectus et netus et malesuada fames ac turpis egestas. Proin pharetra nonummy pede. Mauris et orci.</p>
      <p><b>Aenean nec lorem</b>. In porttitor. Donec laoreet nonummy augue.</p>
      <p>Suspendisse dui purus, scelerisque at, vulputate vitae, pretium mattis, nunc. Mauris eget neque at sem venenatis eleifend. Ut nonummy.</p>
      <p><b>Fusce aliquet pede non pede</b>.<br>Suspendisse dapibus lorem pellentesque magna. Integer nulla.</p>
    </div>
    <footer class="slide-footer">
      <div class="rule"></div>
      <div class="brand">Dorrance</div>
      <div class="pager">
        <svg viewBox="0 0 22 20" aria-hidden="true"><rect width="22" height="20" rx="3" fill="#1b3c6e"/><path d="M13 5 L8 10 L13 15" stroke="#fff" stroke-width="2.6" fill="none"/></svg>
        <svg viewBox="0 0 22 20" aria-hidden="true"><rect width="22" height="20" rx="3" fill="#1b3c6e"/><path d="M9 5 L14 10 L9 15" stroke="#fff" stroke-width="2.6" fill="none"/></svg>
        <span class="sep"></span><span class="num">2</span>
      </div>
    </footer>
  </section>

  <section class="slide slide-services">
    <h2 class="slide-heading"><span class="accent">Our</span> Services</h2>
    <ul class="service-list">
      <li>Lorem ipsum</li><li>Lorem ipsum</li><li>Lorem ipsum</li><li>Lorem ipsum</li><li>Lorem ipsum</li>
      <li>Lorem ipsum</li><li>Lorem ipsum</li><li>Lorem ipsum</li><li>Lorem ipsum</li><li>Lorem ipsum</li>
    </ul>
    <div class="team-photo" role="img" aria-label="Photo of a business team in suits standing together"></div>
    <footer class="slide-footer">
      <div class="rule"></div>
      <div class="brand">Dorrance</div>
      <div class="pager">
        <svg viewBox="0 0 22 20" aria-hidden="true"><rect width="22" height="20" rx="3" fill="#1b3c6e"/><path d="M13 5 L8 10 L13 15" stroke="#fff" stroke-width="2.6" fill="none"/></svg>
        <svg viewBox="0 0 22 20" aria-hidden="true"><rect width="22" height="20" rx="3" fill="#1b3c6e"/><path d="M9 5 L14 10 L9 15" stroke="#fff" stroke-width="2.6" fill="none"/></svg>
        <span class="sep"></span><span class="num">3</span>
      </div>
    </footer>
  </section>

  <section class="slide slide-table">
    <h2 class="slide-heading"><span class="accent">Table</span> Presentation</h2>
    <table class="option-table">
      <thead><tr><th class="cat">CATEGORY</th><th class="o1">OPTION 1</th><th class="o2">OPTION 2</th></tr></thead>
      <tbody>
        <tr class="category"><td colspan="3">Category 1</td></tr>
        <tr class="item"><td>Lorem ipsum dolor sit amet</td><td class="o1">Yes</td><td class="o2">-</td></tr>
        <tr class="item alt"><td>Lorem ipsum dolor sit amet</td><td class="o1">Yes</td><td class="o2">-</td></tr>
        <tr class="item"><td>Lorem ipsum dolor sit amet</td><td class="o1">Yes</td><td class="o2">-</td></tr>
        <tr class="category"><td colspan="3">Category 2</td></tr>
        <tr class="item"><td>Lorem ipsum dolor sit amet</td><td class="o1">Yes</td><td class="o2">-</td></tr>
        <tr class="item alt"><td>Lorem ipsum dolor sit amet</td><td class="o1">Yes</td><td class="o2">-</td></tr>
        <tr class="item"><td>Lorem ipsum dolor sit amet</td><td class="o1">Yes</td><td class="o2">-</td></tr>
        <tr class="item alt"><td>Lorem ipsum dolor sit amet</td><td class="o1">Yes</td><td class="o2">-</td></tr>
        <tr class="category"><td colspan="3">Category 3</td></tr>
        <tr class="item"><td>Lorem ipsum dolor sit amet</td><td class="o1">Yes</td><td class="o2">-</td></tr>
        <tr class="item alt"><td>Lorem ipsum dolor sit amet</td><td class="o1">Yes</td><td class="o2">-</td></tr>
      </tbody>
    </table>
    <footer class="slide-footer">
      <div class="rule"></div>
      <div class="brand">Dorrance</div>
      <div class="pager">
        <svg viewBox="0 0 22 20" aria-hidden="true"><rect width="22" height="20" rx="3" fill="#1b3c6e"/><path d="M13 5 L8 10 L13 15" stroke="#fff" stroke-width="2.6" fill="none"/></svg>
        <svg viewBox="0 0 22 20" aria-hidden="true"><rect width="22" height="20" rx="3" fill="#1b3c6e"/><path d="M9 5 L14 10 L9 15" stroke="#fff" stroke-width="2.6" fill="none"/></svg>
        <span class="sep"></span><span class="num">4</span>
      </div>
    </footer>
  </section>

  <section class="slide slide-contact">
    <h2 class="slide-heading"><span class="accent">Contact</span> Info</h2>
    <div class="map-frame"><div role="img" aria-label="Map of Europe and the Mediterranean region"></div></div>
    <div class="contact-info">
      <p class="intro"><b>Lorem ipsum</b> dolor sit amet, consectetuer adipiscing elit. Maecenas porttitor congue massa. Fusce posuere, magna sed pulvinar ultricies, purus lectus malesuada libero, sit amet commodo magna eros quis urna.</p>
      <h3>Address</h3>
      <p>48 Harbor Lane<br>Fairview, America<br>55210 (U.S.A)</p>
      <h3>Phone</h3>
      <p>0170-555-214</p>
      <h3>FAX</h3>
      <p>0170-555-215</p>
      <h3>Email</h3>
      <p>hello@dorrancefg.example</p>
      <h3>Website</h3>
      <p>www.dorrancefg.example</p>
    </div>
    <div class="social">
      <span class="box"></span><span class="box"></span><span class="box"></span><span class="box"></span>
      <span class="handle">@DORRANCEFG</span>
    </div>
    <footer class="slide-footer">
      <div class="rule"></div>
      <div class="brand">Dorrance</div>
      <div class="pager">
        <svg viewBox="0 0 22 20" aria-hidden="true"><rect width="22" height="20" rx="3" fill="#1b3c6e"/><path d="M13 5 L8 10 L13 15" stroke="#fff" stroke-width="2.6" fill="none"/></svg>
        <svg viewBox="0 0 22 20" aria-hidden="true"><rect width="22" height="20" rx="3" fill="#1b3c6e"/><path d="M9 5 L14 10 L9 15" stroke="#fff" stroke-width="2.6" fill="none"/></svg>
        <span class="sep"></span><span class="num">5</span>
      </div>
    </footer>
  </section>

  <section class="slide slide-thanks">
    <div class="rule" style="left:42px; right:42px; top:61px;"></div>
    <div class="thanks"><span class="accent">Thank</span>You</div>
    <div class="rule" style="left:42px; right:42px; top:207px;"></div>
    <div class="brand thanks-brand">Dorrance</div>
    <div class="blue-band"></div>
  </section>

</main>
</body>
</html>
```